An organizational wellness program flyer - The TALON Program flyer

Need a 2 page PDF and/or tri-fold marketing piece for a program that will be marketed to mid-large employer groups (100-5000 employees). The program is designed to reduce healthcare costs by providing knowledge, tools and techniques to increase employee self-awareness and self-agency. The program details are provided in the uploaded files.
Use the phrase "How much is chronic stress and burnout costing your organization?" as a headline
The designs should highlight the ROI through reduced healthcare costs, employee turnover and absenteeism and increased employee health and engagement.
The description of the TALON acronym should be included and prominent The "Tracks Across Life, Openness and Nurture".
Include The TALON Program framework
Do not include the details of the pathways. Only include the Pathway heading/title.
Have also provided scripts from marketing videos to inform what's included on the flyer, but do not include the scripts on the brochure.
Looking for something clean, not too text heavy but includes the right data points.
Include the phrase "This is not just a program. It's a paradigm shift." at the
Would like all of the source data files so that I can modify later if needed.
Include the BrindleCove logo on the brochure. www.brindlecove.com for brand colors.
organizations with 100-5000 employees; organizations looking for wellness programs
- Clean, compelling visuals
- Images of me on the brochure

```html
<!DOCTYPE html>
<html lang="en">
<head>
<meta charset="utf-8">
<title>The TALON Program – Flyer</title>
<link href="https://fonts.googleapis.com/css2?family=Bebas+Neue&display=swap" rel="stylesheet">
<style>
  :root {
    --canvas: #f5fdf3;
    --paper: #ffffff;
    --forest: #5b8a34;
    --leaf: #84b83a;
    --lime: #b9cc25;
    --bark: #4a3a2a;
    --photo-warm-a: #6b5340;
    --photo-warm-b: #927457;
    --photo-sun-a: #9fc7b8;
    --photo-sun-b: #a7743f;
    --white: #ffffff;
  }
  * { box-sizing: border-box; margin: 0; padding: 0; }
  html, body { width: 1200px; height: 960px; overflow: hidden; background: var(--canvas); }
  body { position: relative; font-family: "Bebas Neue", "Oswald", sans-serif; color: var(--bark); }

  .page {
    position: absolute;
    top: 143px;
    width: 792px;
    height: 1120px;
    background: var(--paper);
    transform: scale(0.635);
    transform-origin: top left;
    box-shadow: 0 10px 40px rgba(60, 90, 40, 0.10);
    overflow: hidden;
  }
  .page--cost { left: 82px; }
  .page--shift { left: 625px; }

  .page__art { position: absolute; inset: 0; width: 792px; height: 1120px; }

  .rule { position: absolute; top: 129px; height: 3px; background: var(--forest); }
  .page--cost .rule { left: 0; width: 540px; }
  .page--shift .rule { left: 7px; width: 783px; }

  .brand {
    position: absolute; top: 30px; right: 10px; width: 220px;
    display: flex; flex-direction: column; align-items: center; gap: 12px;
  }
  .brand__dot { width: 62px; height: 62px; border-radius: 50%; background: var(--leaf); }
  .brand__name { font-size: 40px; letter-spacing: 1px; color: var(--bark); line-height: 1; }

  .headline {
    position: absolute; font-size: 56px; line-height: 67px; color: var(--bark); font-weight: 400;
  }
  .page--cost .headline { left: 52px; top: 168px; }
  .page--shift .headline { right: 62px; top: 168px; text-align: right; }

  .study {
    position: absolute; right: 22px; top: 508px; text-align: right; color: var(--white);
  }
  .study__intro { font-size: 28px; line-height: 1; margin-bottom: 34px; }
  .study__list { list-style: none; }
  .study__item { font-size: 28px; line-height: 38.5px; white-space: nowrap; }
  .study__item::after { content: "  •"; }
  .study__num { color: var(--lime); font-size: 40px; margin-right: 4px; }

  .pathways {
    position: absolute; left: 285px; top: 832px; list-style: none; color: var(--white);
  }
  .pathways li { font-size: 27px; line-height: 32.7px; white-space: nowrap; }
  .pathways li::before { content: "•"; margin-right: 16px; }

  .path-title {
    position: absolute; left: 692px; top: 1100px;
    transform: rotate(-90deg); transform-origin: left top;
    font-size: 78px; line-height: 1; color: var(--bark); white-space: nowrap;
  }
</style>
</head>
<body>

<section class="page page--cost">
  <svg class="page__art" viewBox="0 0 792 1120">
    <defs>
      <linearGradient id="stressTone" x1="0" y1="0" x2="1" y2="1">
        <stop offset="0" stop-color="var(--photo-warm-b)"/>
        <stop offset="1" stop-color="var(--photo-warm-a)"/>
      </linearGradient>
    </defs>
    <path fill="var(--forest)" d="M792,150 C770,235 720,265 640,270 C540,278 470,310 450,390 C432,465 420,520 365,525 C290,530 190,440 100,432 C58,428 48,470 48,520 C50,700 150,860 270,915 C335,940 360,860 400,815 C450,770 560,790 660,905 C720,965 760,995 792,998 Z"/>
    <path role="img" aria-label="Photo of a tired, stressed woman looking at the camera" fill="url(#stressTone)" d="M792,255 C760,330 700,345 600,350 C470,360 460,440 440,490 C420,540 390,555 340,550 C250,540 170,480 80,480 C55,480 48,510 50,540 C60,690 150,840 255,885 C320,905 350,830 400,795 C460,760 560,780 660,880 C720,940 770,960 792,962 Z"/>
  </svg>

  <div class="rule"></div>
  <div class="brand">
    <span class="brand__dot"></span>
    <span class="brand__name">BrindleCove</span>
  </div>

  <h1 class="headline">How much is chronic stress<br>and burnout costing<br>your&nbsp; organization ?</h1>

  <div class="study">
    <p class="study__intro">A recent Harlow study showed :</p>
    <ul class="study__list">
      <li class="study__item"><span class="study__num">25</span>% reported quitting their job due to stress</li>
      <li class="study__item"><span class="study__num">39</span>% needed unplanned leave</li>
      <li class="study__item"><span class="study__num">46</span>stopped caring or mentally checked out of their job</li>
    </ul>
  </div>
</section>

<section class="page page--shift">
  <svg class="page__art" viewBox="0 0 792 1120">
    <defs>
      <linearGradient id="sunTone" x1="0" y1="0" x2="1" y2="1">
        <stop offset="0" stop-color="var(--photo-sun-a)"/>
        <stop offset="0.55" stop-color="var(--photo-sun-b)"/>
        <stop offset="1" stop-color="#7b5230"/>
      </linearGradient>
    </defs>
    <path fill="var(--forest)" d="M0,150 C0,230 40,262 120,270 C230,282 310,305 350,400 C382,478 392,520 450,520 C540,518 620,432 700,430 C738,428 745,470 740,520 C730,640 700,730 640,800 L420,800 C330,820 250,880 170,920 C100,955 40,990 0,998 Z"/>
    <path role="img" aria-label="Photo of a smiling woman with glasses on a sunny beach" fill="url(#sunTone)" d="M0,265 C40,305 100,345 180,350 C270,355 320,385 355,455 C380,505 400,528 450,528 C540,524 620,482 700,480 C735,480 742,520 735,560 C722,680 690,745 640,800 C560,790 420,772 330,802 C260,830 220,880 160,905 C100,925 40,950 0,955 Z"/>
    <path fill="var(--leaf)" d="M30,1125 C150,1110 200,1000 250,880 C292,790 350,770 450,780 C570,792 700,760 794,678 L794,1125 Z"/>
  </svg>

  <div class="rule"></div>

  <h2 class="headline">This is not just a program.<br>It's a paradigm shift.</h2>

  <ul class="pathways">
    <li>The power of emotional regulation</li>
    <li>Getting in sync with your heart's wisdom</li>
    <li>Shifting from disempowered to empowered</li>
    <li>Building a foundation of coherence</li>
    <li>The power of what you believe</li>
    <li>The power of your thoughts</li>
    <li>The power of your subconscious mind</li>
    <li>Stepping into your power</li>
  </ul>

  <p class="path-title">TALON PATH</p>
</section>

</body>
</html>
```